依頼詳細
『コンサルティングのご案内』という冊子を作りたいと思ってます。
原稿はこちらで作成しております。また、会社のロゴもありますので、シンプルなデザインを組み合わせていただいて、上品で高品質な印象を持ってもらえるような冊子ができたらいいなと思っております。
記載項目
①表紙は『コンサルティングのご案内』という文章とデザイン
②③は原稿がありますので、それにシンプルなデザインを組み合わせ
④ロゴとシンプルなデザイン

イメージは上記のような感じですが、絶対ではありませんので、デザイナーさんのセンスにお任せいたします。
サイズ
A4
ページ数
4ページ
希望イメージ
シンプル 複雑
単色 カラフル
暗い 明るい
日常 高級
遊び心 厳粛
未来的 伝統的
女性的 男性的
希望する色
紙で高級感を出そうと思っておりますので、白がベースかなと思っております。
補足説明
PDFでの納品が希望です。
納品物は作成いただいたデータでもお願いします。
追記です。

会社案内の冊子は別にありますので、会社案内的な要素を入れる必要はありません。

新たに『コンサルティングのご案内』、という別冊子を作る趣旨は、そこだけを取り上げた冊子を作りたいからです。

デザインも会社案内的な特徴を出すために少し派手な印象を入れる、というのとは真逆で、むしろ少し控えめにするくらいで、本当にシンプルでワンポイント的なデザインの方がいいです。

イメージとしては、高級フレンチ料理のメニュー表、とか、結婚式のメニュー表、のようなそんな感じの冊子ができればいいと思っております。

よろしくお願いいたします。
■ 選んだ理由

最も趣旨を汲んでくださった提案でしたので、選出させていただきました。

シンプルの中にも、高級感と奥深さを感じられ、ただの紙にとどまらず、全体のデザインから、質の高いコンサルティングを受けることができそうだと、思っていただけるような、デザインからそういった力を感じさせることができるような、素晴らしいデザインだったと思います。

■ 提案者全員のお礼・コメント

この度は、ご多忙にもかかわらず、たくさんの方にご提案をいただきまして、誠にありがとうございました。
素晴らしい提案がとても多く、非常に贅沢な悩みで、選出させていただきました。
このような形でしか御礼をお伝えすることができず、心苦しい点もありますが、気にかけていただき、そして、お時間を使っていただき、ご提案いただきましたことに、心から感謝申し上げます。
またぜひ次の機会にご縁をいただければ、大変嬉しく思います。
ありがとうございました。

```html
<!DOCTYPE html>
<html lang="ja">
<head>
<meta charset="utf-8">
<title>コンサルティングのご案内</title>
<link rel="stylesheet" href="https://fonts.googleapis.com/css2?family=Shippori+Mincho:wght@500&family=Noto+Sans+JP:wght@400&display=swap">
<style>
  :root {
    --paper: #ffffff;
    --pattern-top: #ece6dc;
    --pattern-mid: #f4f0ea;
    --ink: #3a3330;
    --mark: #a8322b;
    --frame-gold: #c9b48a;
    --label-grey: #6b6662;
  }
  html, body {
    margin: 0;
    padding: 0;
    width: 879px;
    height: 1200px;
    overflow: hidden;
    background: var(--paper);
  }
  .cover {
    position: relative;
    width: 879px;
    height: 1200px;
    background: var(--paper);
  }
  .cover-pattern {
    position: absolute;
    left: 0;
    top: 0;
    width: 879px;
    height: 640px;
    background:
      linear-gradient(to bottom, rgba(255,255,255,0) 55%, var(--paper) 100%),
      linear-gradient(200deg, var(--pattern-top) 0%, var(--pattern-mid) 45%, var(--paper) 85%);
  }
  .brand {
    position: absolute;
    left: 0;
    top: 738px;
    width: 879px;
    display: flex;
    flex-direction: column;
    align-items: center;
  }
  .brand-dot {
    width: 62px;
    height: 62px;
    border-radius: 50%;
    background: var(--mark);
  }
  .brand-name {
    margin-top: 26px;
    font-family: "Shippori Mincho", serif;
    font-weight: 500;
    font-size: 40px;
    letter-spacing: 4px;
    color: var(--ink);
  }
  .title-label {
    position: absolute;
    left: 50%;
    top: 1018px;
    transform: translateX(-50%);
    width: 440px;
    height: 42px;
    box-sizing: border-box;
    border: 1.5px solid var(--frame-gold);
    border-radius: 21px;
    display: flex;
    align-items: center;
    justify-content: center;
    font-family: "Noto Sans JP", sans-serif;
    font-size: 19px;
    letter-spacing: 2px;
    color: var(--label-grey);
  }
</style>
</head>
<body>
  <main class="cover">
    <div class="cover-pattern" role="img" aria-label="Soft white and beige geometric hexagonal cube pattern fading downward"></div>
    <div class="brand">
      <div class="brand-dot"></div>
      <div class="brand-name">和匠継承</div>
    </div>
    <h1 class="title-label">コンサルティングのご案内</h1>
  </main>
</body>
</html>
```